Harrow grounds and gardens

Lawn Maintenance, Spring Fall Clean Ups, Stone Walls & Walkways, Commercial and Residental Snow Removal carpentry and handyman services

Industry/Entity Type

Carpentry

Contact Information for Business Card

Harrow Grounds and Gardens 83 Copper Fern Rd Monticello NY 12701 555 302 8419 Cell 555216 9083

```html
<!DOCTYPE html>
<html lang="en">
<head>
<meta charset="utf-8">
<title>Harrow Grounds and Gardens – Business Card</title>
<link rel="stylesheet" href="https://fonts.googleapis.com/css2?family=Michroma&display=swap">
<style>
  :root {
    --page-bg: #ffffff;
    --sky-top: #0839a8;
    --sky-mid: #1a7fd8;
    --sky-bottom: #3fd0f4;
    --ink: #000000;
    --turf-dark: #010601;
    --turf-green: #3fd21a;
    --figure-tone: #06162c;
  }
  * { margin: 0; padding: 0; box-sizing: border-box; }
  html, body {
    width: 1200px;
    height: 1200px;
    overflow: hidden;
    background: var(--page-bg);
  }
  .business-card {
    position: absolute;
    left: 50px;
    top: 288px;
    width: 1100px;
    height: 625px;
    overflow: hidden;
    background: linear-gradient(180deg, var(--sky-top) 0%, var(--sky-mid) 45%, var(--sky-bottom) 100%);
    font-family: "Michroma", sans-serif;
    color: var(--ink);
    font-variant: small-caps;
  }
  .mower-figure {
    position: absolute;
    left: 40px;
    top: 48px;
    width: 560px;
    height: 466px;
    z-index: 1;
  }
  .turf-band {
    position: absolute;
    left: 0;
    bottom: 0;
    width: 100%;
    height: 113px;
    background: linear-gradient(180deg, var(--turf-green) 0%, #1c7a0e 30%, var(--turf-dark) 100%);
    z-index: 2;
  }
  .card-text {
    position: absolute;
    right: 57px;
    text-align: right;
    white-space: nowrap;
    z-index: 3;
  }
  .business-name {
    top: 6px;
    font-size: 47px;
    font-weight: 400;
    line-height: 76px;
    letter-spacing: 0.14em;
    font-variant: normal;
    text-transform: uppercase;
  }
  .service-line {
    top: 164px;
    font-size: 26px;
    letter-spacing: 0.03em;
  }
  .contact-block {
    top: 228px;
    font-size: 27px;
    line-height: 32px;
    letter-spacing: 0.08em;
  }
  .contact-block .heading {
    font-variant: normal;
    text-transform: uppercase;
    font-size: 25px;
  }
  .address-block {
    top: 345px;
    font-size: 27px;
    line-height: 40px;
    letter-spacing: 0.08em;
    font-style: normal;
  }
</style>
</head>
<body>
  <main class="business-card">
    <svg class="mower-figure" role="img" aria-label="Silhouette of a person pushing a lawn mower across the grass" viewBox="0 0 560 466">
      <defs>
        <linearGradient id="figureShade" x1="0" y1="0" x2="0" y2="1">
          <stop offset="0%" stop-color="var(--figure-tone)" stop-opacity="0.05"/>
          <stop offset="60%" stop-color="var(--figure-tone)" stop-opacity="0.22"/>
          <stop offset="100%" stop-color="var(--figure-tone)" stop-opacity="0.4"/>
        </linearGradient>
      </defs>
      <rect x="0" y="0" width="560" height="466" rx="40" fill="url(#figureShade)"/>
    </svg>

    <h1 class="card-text business-name">Harrow Grounds and<br>Gardens</h1>

    <p class="card-text service-line">Lawn Maintenance, Stone Walls &amp; Walkways, Commercial and Residental Snow Removal, carpentry, Spring Fall Clean Ups,handyman services</p>

    <div class="card-text contact-block">
      <p class="heading">Handyman Services</p>
      <p>Ph: 555 302 8419 Mbl: 555 216 9083</p>
      <p>Mbl: 555 216 9083</p>
    </div>

    <address class="card-text address-block">
      <p>83 Copper Fern Rd</p>
      <p>Monticello NY 12701</p>
    </address>

    <div class="turf-band" role="img" aria-label="Band of green grass blades along the bottom"></div>
  </main>
</body>
</html>
```